Letterhead for New Orthopaedic Surgery Practice

My husband and I are starting our own practice named RB Spine & Vitality Center. We would like to create a nice simple but high class letterhead that doesn't use too much solid color ink when printing. I like the colors dark blue, gold, yellow. Open to other suggestions. We will need to list him and I both on the top of the letterhead. Here is the important information:
Lucinda Perrow, M.D. - Hand and Upper Extremity Surgery
Abena Quist, M.D. - Hip & Knee Replacement/General Orthopaedic Surgery
Location: 18735 North Harlow Pkwy
Coral Springs, FL 33071
Phone: 954-218-4650
Fax: 954-582-1346
Email: info@myrbspine.com

The only thing is that the phone and fax numbers will change once we get into our space. I just want to get the design started. I am including several documents which are my previous practice letterhead, my current procedure room letterhead, and our new Logo. The other letterheads are just for examples but please think outside of the box! We would love to see some great designs.

Colors
0054AA
0677BA
7BADD7
CADEEF
E8F1F8
0094D4
00A9DD
6FCCEA
C7EBF8
E9F6FB

Requirements
Must have
• class, elegance, luxury

```html
<!DOCTYPE html>
<html lang="en">
<head>
<meta charset="UTF-8">
<title>RB Spine &amp; Vitality Center — Letterhead</title>
<link rel="stylesheet" href="https://fonts.googleapis.com/css2?family=Noto+Serif:wght@400;700&family=Roboto:wght@400&display=swap">
<style>
  :root {
    --backdrop: #dcdcdc;
    --paper: #f8f8f8;
    --navy: #15244a;
    --gold: #c9a35a;
    --body-grey: #555a60;
    --watermark: #e7e8ec;
  }
  * { margin: 0; padding: 0; box-sizing: border-box; }
  html, body {
    width: 1153px;
    height: 1200px;
    overflow: hidden;
    background: var(--backdrop);
  }
  .letterhead {
    position: absolute;
    left: 151px;
    top: 50px;
    width: 850px;
    height: 1100px;
    background: var(--paper);
    box-shadow: 0 6px 18px rgba(0,0,0,0.12);
    overflow: hidden;
  }
  .brand-mark {
    position: absolute;
    left: 84px;
    top: 86px;
    display: flex;
    align-items: center;
    gap: 12px;
  }
  .brand-dot {
    width: 14px;
    height: 14px;
    border-radius: 50%;
    background: var(--gold);
  }
  .brand-name {
    font-family: "Noto Serif", serif;
    font-weight: 700;
    font-size: 17px;
    line-height: 1.3;
    color: var(--navy);
  }
  .contact-block {
    position: absolute;
    left: 572px;
    top: 76px;
    height: 104px;
    padding-left: 18px;
    border-left: 1px solid var(--gold);
    font-family: "Roboto", sans-serif;
    font-style: normal;
    font-size: 14px;
    color: var(--body-grey);
    line-height: 19px;
  }
  .contact-address { margin-bottom: 4px; }
  .contact-line {
    display: flex;
    align-items: center;
    gap: 7px;
    line-height: 21px;
  }
  .contact-icon { width: 14px; height: 14px; fill: var(--navy); flex: none; }
  .watermark-name {
    position: absolute;
    left: 0;
    right: 0;
    top: 450px;
    text-align: center;
    font-family: "Noto Serif", serif;
    font-weight: 700;
    color: var(--watermark);
    line-height: 1;
  }
  .watermark-initials { font-size: 230px; display: block; }
  .watermark-words { font-size: 40px; display: block; margin-top: 10px; }
  .physician {
    position: absolute;
    top: 996px;
    font-family: "Noto Serif", serif;
    font-size: 16px;
    line-height: 20px;
    color: var(--body-grey);
  }
  .physician-left { left: 84px; }
  .physician-right { right: 87px; text-align: right; }
  .physician-name { font-weight: 700; color: var(--navy); }
</style>
</head>
<body>
  <main class="letterhead">
    <div class="brand-mark">
      <span class="brand-dot"></span>
      <div class="brand-name">RB Spine &amp;<br>Vitality Center</div>
    </div>

    <address class="contact-block">
      <div class="contact-address">18735 North Harlow Pkwy<br>Coral Springs, FL 33071</div>
      <div class="contact-line">
        <svg class="contact-icon" viewBox="0 0 16 16" aria-hidden="true"><path d="M1 6c0-2 3-3 7-3s7 1 7 3v1h-3V5.5c-1-.4-2.5-.5-4-.5s-3 .1-4 .5V7H1z"/><path d="M3 9l2-3h6l2 3v5H3z"/><circle cx="8" cy="10.5" r="1.6" fill="#f8f8f8"/></svg>
        <span>954-218-4650</span>
      </div>
      <div class="contact-line">
        <svg class="contact-icon" viewBox="0 0 16 16" aria-hidden="true"><path d="M4 1h8v5H4z"/><path d="M1 7h14v6H1z"/><rect x="4" y="10" width="8" height="5" fill="#f8f8f8" stroke="#15244a" stroke-width="1.2"/></svg>
        <span>954-582-1346</span>
      </div>
      <div class="contact-line">
        <svg class="contact-icon" viewBox="0 0 16 16" aria-hidden="true"><path d="M1 3h14v10H1z"/><path d="M1 3l7 5 7-5" fill="none" stroke="#f8f8f8" stroke-width="1.4"/></svg>
        <span>info@myrbspine.com</span>
      </div>
    </address>

    <div class="watermark-name" aria-hidden="true">
      <span class="watermark-initials">RB</span>
      <span class="watermark-words">Spine &amp; Vitality Center</span>
    </div>

    <div class="physician physician-left">
      <div class="physician-name">Lucinda Perrow, M.D.</div>
      <div>Hand and Upper</div>
      <div>Extremity Surgery</div>
    </div>
    <div class="physician physician-right">
      <div class="physician-name">Abena Quist, M.D.</div>
      <div>Hip &amp; Knee Replacement</div>
      <div>General Orthopaedic Surgery</div>
    </div>
  </main>
</body>
</html>
```